Lexora: Legal Flyer

We need an A5 double sided leaflet that is not too congested with writing but gets all the necessary information across.

We want the leaflet to look clean and professional but also colourful and something that entices people to read it.

The message we want to subtly convey is that knowledge is power and Lexora:Legal is the fountain to their legal knowledge. Or alternatively Lexora:Legal is like a filter that sucks in all the legal jargon typically used by lawyers and produces easy to digest and understandable information.

Our slogan is Lexora:Legal... We educate to empower.
Please feel free to visit our site www.LexoraLegal.co.uk for more information on what we do or to gain inspiration from the site to ensure both the leaflet and site complement one another.

With that being said, please feel free to be as creative as you please.

Target Market(s)

People who have no legal knowledge. Our core audience are 25-35 years old while our subsidiary audience are 18 - 25 years old.

Industry/Entity Type

Legal

Requirements
Must have
• Our Logo
Our facebook : www.facebook.com/LexoraLegal
Our twtter: @LexoraLegal
Our website www.LexoraLegal.co.uk
Nice to have
• Some nice creative illustrations.
Should not have
• Boring typical law related photographs.

```html
<!DOCTYPE html>
<html lang="en">
<head>
<meta charset="utf-8">
<title>Lexora: Legal — Leaflet</title>
<link rel="stylesheet" href="https://fonts.googleapis.com/css2?family=Great+Vibes&family=Raleway:wght@300;400;500&family=Barlow:wght@400;500&family=Barlow+Semi+Condensed:wght@400;500&display=swap">
<style>
  :root {
    --page: #3d3d3d;
    --sky-top: #a9cde8;
    --sky-mid: #d8ebf6;
    --sky-low: #8fbfe2;
    --stone: #b8734e;
    --band: rgba(255, 255, 255, 0.74);
    --strip: #5e9fd6;
    --ink-grey: #5a5a5c;
    --brand-red: #e0174b;
    --back-dark: #1c0d08;
    --back-mid: #4a2414;
    --back-warm: #6b3a1f;
    --paper-white: #f4eee9;
    --rule: rgba(255, 255, 255, 0.55);
    --heading-red: #ef2b55;
  }
  * { box-sizing: border-box; margin: 0; padding: 0; }
  html, body { width: 801px; height: 1200px; overflow: hidden; }
  body { background: var(--page); position: relative; font-family: "Barlow", sans-serif; }

  .side { position: absolute; left: 56px; width: 688px; height: 487px; overflow: hidden; }
  .side--front { top: 65px; }
  .side--back { top: 654px; }

  /* FRONT */
  .front-photo {
    position: absolute; inset: 0;
    background:
      radial-gradient(ellipse 170px 300px at 560px 330px, rgba(184,115,78,0.85), rgba(184,115,78,0) 100%),
      linear-gradient(170deg, var(--sky-top) 0%, var(--sky-mid) 35%, var(--sky-top) 65%, var(--sky-low) 100%);
  }
  .slogan {
    position: absolute; top: 38px; left: 0; right: 0; text-align: center;
    font-family: "Great Vibes", cursive; font-size: 47px; color: var(--ink-grey);
    letter-spacing: 1px;
  }
  .brand-band { position: absolute; left: 0; right: 0; top: 290px; height: 128px; background: var(--band); }
  .brand-name {
    position: absolute; left: 20px; top: 322px;
    font-family: "Raleway", sans-serif; font-weight: 400; font-size: 58px;
    color: var(--ink-grey); letter-spacing: -1px; line-height: 1;
  }
  .site-url {
    position: absolute; right: 18px; top: 382px;
    font-family: "Raleway", sans-serif; font-weight: 500; font-size: 18.5px; color: var(--brand-red);
  }
  .contact-strip { position: absolute; left: 0; right: 0; bottom: 0; height: 69px; background: var(--strip); opacity: 0.9; }
  .contacts { position: absolute; left: 121px; top: 440px; display: flex; gap: 24px; align-items: center; }
  .contact { display: flex; align-items: center; gap: 7px; font-family: "Raleway", sans-serif; font-weight: 500; font-size: 12px; color: var(--brand-red); }
  .contact-mark { width: 16px; height: 16px; border-radius: 3px; background: #e9eef3; display: block; }
  .contact svg { display: block; }

  /* BACK */
  .back-photo {
    position: absolute; inset: 0;
    background:
      radial-gradient(ellipse 260px 200px at 470px 300px, rgba(150,95,50,0.45), rgba(0,0,0,0) 100%),
      radial-gradient(ellipse 420px 320px at 380px 220px, var(--back-warm), var(--back-mid) 55%, var(--back-dark) 100%);
  }
  .section-title {
    position: absolute; left: 0; right: 0; text-align: center;
    font-family: "Raleway", sans-serif; font-weight: 400; font-size: 20px; letter-spacing: 3px; color: var(--paper-white);
  }
  .section-title--about { top: 24px; }
  .section-title--services { top: 302px; }
  .divider { position: absolute; }
  .col { position: absolute; top: 83px; color: var(--paper-white); }
  .col h3 {
    font-family: "Barlow Semi Condensed", sans-serif; font-weight: 500; font-size: 11px;
    color: var(--heading-red); text-align: center; margin-bottom: 5px; letter-spacing: 0.3px;
  }
  .col p { font-size: 8.4px; line-height: 11.2px; text-align: justify; }
  .col p + p { margin-top: 11px; }
  .col--who { left: 31px; width: 154px; }
  .col--why { left: 204px; width: 277px; }
  .col--what { left: 489px; width: 172px; }
  .offer-list { list-style: none; font-size: 8.4px; line-height: 11.2px; }
  .offer-list li { position: relative; padding-left: 10px; text-align: justify; margin-bottom: 5px; }
  .offer-list li svg { position: absolute; left: 0; top: 2px; }

  .services { position: absolute; top: 338px; left: 0; right: 0; }
  .service-col { position: absolute; top: 0; list-style: none; }
  .service-col li {
    position: relative; padding-left: 15px; height: 21.5px;
    font-family: "Barlow Semi Condensed", sans-serif; font-weight: 500; font-size: 13.5px; color: var(--paper-white);
  }
  .service-col li svg { position: absolute; left: 0; top: 4px; }
  .service-note { display: block; font-size: 9px; line-height: 10px; font-weight: 400; margin-top: 1px; }
  .service-col--a { left: 44px; }
  .service-col--b { left: 198px; }
  .service-col--c { left: 334px; }
  .service-col--d { left: 488px; }
</style>
</head>
<body>

<section class="side side--front" aria-label="Leaflet front">
  <div class="front-photo" role="img" aria-label="Blue sky with clouds behind a stone statue of blindfolded Justice holding scales"></div>
  <p class="slogan">Legal we educate to empower</p>
  <div class="brand-band"></div>
  <div class="brand-name">Lexora Legal</div>
  <div class="site-url">www.LexoraLegal.co.uk</div>
  <div class="contact-strip"></div>
  <div class="contacts">
    <span class="contact"><span class="contact-mark"></span>LexoraLegal</span>
    <span class="contact"><span class="contact-mark"></span>@LexoraLegal</span>
    <span class="contact">
      <svg width="17" height="13" viewBox="0 0 17 13"><rect x="0.5" y="0.5" width="16" height="12" rx="1.5" fill="#eef2f6" stroke="#6d7b8a"/><path d="M1 1.5 L8.5 7.5 L16 1.5" fill="none" stroke="#6d7b8a" stroke-width="1.2"/></svg>
      Enquiries@LexoraLegal.co.uk
    </span>
  </div>
</section>

<section class="side side--back" aria-label="Leaflet back">
  <div class="back-photo" role="img" aria-label="Dark warm-toned close-up of brass justice scales"></div>

  <h2 class="section-title section-title--about">ABOUT US</h2>
  <svg class="divider" style="left:100px; top:59px" width="490" height="12" viewBox="0 0 490 12">
    <line x1="8" y1="6" x2="482" y2="6" stroke="var(--rule)" stroke-width="1"/>
    <circle cx="8" cy="6" r="4" fill="var(--paper-white)"/>
    <circle cx="242" cy="6" r="4" fill="var(--paper-white)"/>
    <circle cx="482" cy="6" r="4" fill="var(--paper-white)"/>
  </svg>

  <div class="col col--who">
    <h3>WHO WE ARE</h3>
    <p>The Lexora: Legal team, are LLB Law graduates from Northmere University, Canterbury and the University of Eastmarsh. Our degrees and work placements have equipped us with extensive legal knowledge and legal research skills, allowing us to provide information and guidance to those in need of it. Whether it be making people aware of how courts have dealt with cases similar to their own in the past, or simply referring them to an organisation that can provide more assistance.</p>
  </div>

  <div class="col col--why">
    <h3>WHY WE DO / WHAT WE DO</h3>
    <p>Lexora: Legal was created in response to a number of social issues, the primary reason being the introduction of the 2012 Legal Aid, Sentencing and Punishment Act. The reforms removed social welfare law from the scope of legal aid, reducing the funding that law centres rely on by over 39%. The £20 million slash to the budget left many centres with no option but to close down, leaving thousands without access to justice. Put simply, we identified a problem and aim to provide solutions that will reinstate some services reduced by legal aid reforms.</p>
    <p>The aim of Lexora: Legal is to bridge the gap between the average citizen and the English and Welsh Legal system. Our desire is to equip and empower people with legal knowledge allowing them to confidently take the right steps to best resolve their legal issues.</p>
  </div>

  <div class="col col--what">
    <h3>WHAT WE CAN DO FOR YOU</h3>
    <ul class="offer-list">
      <li><svg width="7" height="6" viewBox="0 0 7 6"><path d="M0.5 3 L2.6 5 L6.5 0.8" fill="none" stroke="var(--paper-white)" stroke-width="1.4"/></svg>We offer our service via our website in order to ensure maximum accessibility.</li>
      <li><svg width="7" height="6" viewBox="0 0 7 6"><path d="M0.5 3 L2.6 5 L6.5 0.8" fill="none" stroke="var(--paper-white)" stroke-width="1.4"/></svg>We provide useful legal hints and tips allowing users to educate themselves on various legal issues.</li>
      <li><svg width="7" height="6" viewBox="0 0 7 6"><path d="M0.5 3 L2.6 5 L6.5 0.8" fill="none" stroke="var(--paper-white)" stroke-width="1.4"/></svg>We facilitate the submission of legal queries.</li>
      <li><svg width="7" height="6" viewBox="0 0 7 6"><path d="M0.5 3 L2.6 5 L6.5 0.8" fill="none" stroke="var(--paper-white)" stroke-width="1.4"/></svg>We acknowledge all queries within 72 hours of receiving them and keep users well informed throughout the whole process.</li>
    </ul>
  </div>

  <h2 class="section-title section-title--services">SERVICES</h2>
  <svg class="divider" style="left:46px; top:329px" width="596" height="2" viewBox="0 0 596 2">
    <line x1="0" y1="1" x2="596" y2="1" stroke="var(--rule)" stroke-width="1"/>
  </svg>

  <div class="services">
    <ul class="service-col service-col--a">
      <li><svg width="10" height="9" viewBox="0 0 10 9"><path d="M1 4.5 L3.8 7.5 L9 1.2" fill="none" stroke="var(--brand-red)" stroke-width="2.2"/></svg>Banking Law</li>
      <li><svg width="10" height="9" viewBox="0 0 10 9"><path d="M1 4.5 L3.8 7.5 L9 1.2" fill="none" stroke="var(--brand-red)" stroke-width="2.2"/></svg>Commercial Law</li>
      <li><svg width="10" height="9" viewBox="0 0 10 9"><path d="M1 4.5 L3.8 7.5 L9 1.2" fill="none" stroke="var(--brand-red)" stroke-width="2.2"/></svg>Equity Law</li>
      <li><svg width="10" height="9" viewBox="0 0 10 9"><path d="M1 4.5 L3.8 7.5 L9 1.2" fill="none" stroke="var(--brand-red)" stroke-width="2.2"/></svg>Policing<span class="service-note">(Including: Police powers of<br>Stop &amp; Search, Arrest, Detention<br>&amp; Questioning, Public order)</span></li>
    </ul>
    <ul class="service-col service-col--b">
      <li><svg width="10" height="9" viewBox="0 0 10 9"><path d="M1 4.5 L3.8 7.5 L9 1.2" fill="none" stroke="var(--brand-red)" stroke-width="2.2"/></svg>Company Law</li>
      <li><svg width="10" height="9" viewBox="0 0 10 9"><path d="M1 4.5 L3.8 7.5 L9 1.2" fill="none" stroke="var(--brand-red)" stroke-width="2.2"/></svg>Consumer Law</li>
      <li><svg width="10" height="9" viewBox="0 0 10 9"><path d="M1 4.5 L3.8 7.5 L9 1.2" fill="none" stroke="var(--brand-red)" stroke-width="2.2"/></svg>Family Law</li>
      <li><svg width="10" height="9" viewBox="0 0 10 9"><path d="M1 4.5 L3.8 7.5 L9 1.2" fill="none" stroke="var(--brand-red)" stroke-width="2.2"/></svg>Land Law</li>
    </ul>
    <ul class="service-col service-col--c">
      <li><svg width="10" height="9" viewBox="0 0 10 9"><path d="M1 4.5 L3.8 7.5 L9 1.2" fill="none" stroke="var(--brand-red)" stroke-width="2.2"/></svg>Contract Law</li>
      <li><svg width="10" height="9" viewBox="0 0 10 9"><path d="M1 4.5 L3.8 7.5 L9 1.2" fill="none" stroke="var(--brand-red)" stroke-width="2.2"/></svg>Criminal Law</li>
      <li><svg width="10" height="9" viewBox="0 0 10 9"><path d="M1 4.5 L3.8 7.5 L9 1.2" fill="none" stroke="var(--brand-red)" stroke-width="2.2"/></svg>Property Law</li>
      <li><svg width="10" height="9" viewBox="0 0 10 9"><path d="M1 4.5 L3.8 7.5 L9 1.2" fill="none" stroke="var(--brand-red)" stroke-width="2.2"/></svg>Tort<span class="service-note">(Negligence, Civil Wrongs,<br>Occupiers Liability, Trespass<br>and Nuisance)</span></li>
    </ul>
    <ul class="service-col service-col--d">
      <li><svg width="10" height="9" viewBox="0 0 10 9"><path d="M1 4.5 L3.8 7.5 L9 1.2" fill="none" stroke="var(--brand-red)" stroke-width="2.2"/></svg>Employment Relations</li>
      <li><svg width="10" height="9" viewBox="0 0 10 9"><path d="M1 4.5 L3.8 7.5 L9 1.2" fill="none" stroke="var(--brand-red)" stroke-width="2.2"/></svg>Environmental Law</li>
      <li><svg width="10" height="9" viewBox="0 0 10 9"><path d="M1 4.5 L3.8 7.5 L9 1.2" fill="none" stroke="var(--brand-red)" stroke-width="2.2"/></svg>Trust Law</li>
      <li><svg width="10" height="9" viewBox="0 0 10 9"><path d="M1 4.5 L3.8 7.5 L9 1.2" fill="none" stroke="var(--brand-red)" stroke-width="2.2"/></svg>European Union Law</li>
    </ul>
  </div>
</section>

</body>
</html>
```